Business Card Design Project

Hi

I have a draft of a business card which I need smarting up. I have attached the pdf of this.
The information on the front is correct.
The information on the back should contain:
Project Management, Consulting, Master Systems Integrator, Datacenter, Relocations, Restacks. I want this spiraling around the back

Can you change the telephone number to +65 8476 2153.

Target Market(s)

Chief Technology Officers of large multi-nationals

Industry/Entity Type

Business

Requirements
Must have
• My logo - Vorbelt (attached)
The orange and blue colour running around the edge

```html
<!DOCTYPE html>
<html lang="en">
<head>
<meta charset="utf-8">
<title>Vorbelt Business Card</title>
<link rel="stylesheet" href="https://fonts.googleapis.com/css2?family=Arimo:wght@400;700&display=swap">
<style>
  :root {
    --orange: #f08a1c;
    --blue: #5fd3e0;
    --card-black: #0b0b0b;
    --card-white: #f7f7f5;
    --ink: #1e1e1e;
    --wordmark-grey: #3c3c3c;
    --muted-grey: #9a9a9a;
    --backdrop: #2b2b2b;
  }
  * { box-sizing: border-box; margin: 0; padding: 0; }
  html, body {
    width: 1200px; height: 900px; overflow: hidden;
    background: var(--backdrop);
    font-family: "Arimo", Arial, sans-serif;
  }
  .stage {
    position: relative; width: 1200px; height: 900px;
    display: flex; align-items: center; justify-content: center; gap: 40px;
  }
  .card {
    position: relative; width: 540px; height: 324px;
    border-radius: 6px; overflow: hidden;
    box-shadow: 0 10px 30px rgba(0,0,0,0.45);
  }
  .card-frame {
    position: absolute; inset: 16px;
    border: 3px solid var(--orange); border-radius: 18px;
  }

  /* Back */
  .card-back { background: var(--card-black); }
  .service-list {
    position: absolute; left: 38px; top: 44px;
    list-style: none; color: var(--blue);
    font-size: 14px; letter-spacing: 1.2px; line-height: 19px;
  }
  .back-brand {
    position: absolute; left: 250px; top: 130px;
    display: flex; align-items: center; gap: 14px;
  }
  .back-brand .brand-dot {
    width: 18px; height: 18px; border-radius: 50%;
    background: var(--blue);
  }
  .back-brand .brand-name {
    color: var(--muted-grey); font-size: 36px; letter-spacing: 0.5px;
  }

  /* Front */
  .card-front { background: var(--card-white); }
  .front-brand {
    position: absolute; left: 24px; top: 24px;
    display: flex; align-items: center; gap: 14px;
  }
  .front-brand .brand-square {
    width: 56px; height: 56px; border-radius: 10px;
    background: #2a2a2a;
  }
  .front-brand .brand-name {
    color: var(--wordmark-grey); font-size: 40px; letter-spacing: 0.5px;
  }
  .person { position: absolute; left: 42px; top: 142px; }
  .person-name { color: var(--orange); font-size: 20px; }
  .person-role { color: var(--ink); font-size: 10px; margin-top: 3px; }
  .address {
    position: absolute; left: 42px; top: 214px;
    font-style: normal; color: var(--ink);
    font-size: 11.5px; letter-spacing: 0.8px; line-height: 15px;
  }
  .contact {
    position: absolute; left: 262px; top: 212px;
    padding-left: 14px; border-left: 1.5px solid var(--ink);
    list-style: none; color: var(--ink);
    font-size: 12px; letter-spacing: 1px; line-height: 17px;
  }
  .contact-label { color: var(--orange); display: inline-block; width: 18px; }
</style>
</head>
<body>
<main class="stage">
  <section class="card card-back" aria-label="Business card back">
    <div class="card-frame"></div>
    <ul class="service-list">
      <li>Master Systems Integrator</li>
      <li>Project Management</li>
      <li>Consulting</li>
      <li>Datacenter</li>
      <li>Relocations</li>
      <li>Restacks</li>
    </ul>
    <div class="back-brand">
      <span class="brand-dot"></span>
      <span class="brand-name">Vorbelt</span>
    </div>
  </section>

  <section class="card card-front" aria-label="Business card front">
    <div class="card-frame"></div>
    <div class="front-brand">
      <span class="brand-square"></span>
      <span class="brand-name">Vorbelt</span>
    </div>
    <div class="person">
      <p class="person-name">Marcus Hale</p>
      <p class="person-role">Director</p>
    </div>
    <address class="address">
      Vorbelt Pte Ltd, 21 Harbour Crescent<br>
      #05-12 Bayfront Plaza<br>
      Singapore, 049312
    </address>
    <ul class="contact">
      <li><span class="contact-label">T:</span>+65 8476 2153</li>
      <li><span class="contact-label">E:</span>marcus.hale@vorbelt.com</li>
      <li><span class="contact-label">W:</span>www.vorbelt.com</li>
    </ul>
  </section>
</main>
</body>
</html>
```